Design for Tolvo Ginger Chewy Candy!

Hello! We are Tolvo Enterprises Corp, a food manufacturer and distributor based in Los Angeles, CA. We manufacture Chips, Cookies, Juices, Dairy, and last but not least, Candies! We are launching our Ginger Chewy Candy soon and we need a great design for it!

Our Ginger Chewy Candy is a perfect mixture between sweet and spicy from the ginger itself. Tolvo Ginger Chewy Candy a good relief for sore throat and nausea.

Now, other than a great design, we also welcome brand suggestions for the candy.
If you can come up with a logo for the Ginger Candy, that would be swell!

We are open to unique and out of the box design. We chose a few color schemes for the design, but feel free to step out of the box if you feel it suits the brand.

We don't have the exact size for the plastic pouch, but it should be a generic small plastic pouch size (approximately 4 oz resealable plastic pouch)

Please have fun designing the project, we can't wait to see all the great designs!

Cheers!

Target Market(s)

USA and Asian market
Age 30-70
Male and Female

Industry/Entity Type

Manufacture

Font styles to use
Serif
Sans Serif
Decorative

Colors
fff3d1
fee18a
fece3e
fbc994
fce8d3

Requirements
Must have
• Tolvo Logo
• A picture of ginger (illustrations or photographs are welcome)
Nice to have
• Coating suggestions like Matte surface or SPOT UV
• Give us ideas of what the name of the chewy candy should be. Product name ideas are welcome!

```html
<!DOCTYPE html>
<html lang="en">
<head>
<meta charset="utf-8">
<title>Tolvo Ginger Candy Pouch</title>
<link rel="stylesheet" href="https://fonts.googleapis.com/css2?family=Damion&family=Quicksand:wght@500;600&display=swap">
<style>
  :root {
    --page-bg: #ffffff;
    --pouch-white: #fdfdfc;
    --cream: #fff3d1;
    --butter: #fee18a;
    --sun: #fece3e;
    --ginger-orange: #f6a623;
    --candy-yellow: #f8c42c;
    --brand-blue: #2b4f9e;
    --leaf-green: #3aa648;
    --root-tan: #e2b98f;
    --slice-yellow: #f3dc7a;
  }
  * { margin: 0; padding: 0; box-sizing: border-box; }
  html, body {
    width: 960px;
    height: 1200px;
    overflow: hidden;
    background: var(--page-bg);
  }
  .canvas {
    position: relative;
    width: 960px;
    height: 1200px;
    background: var(--page-bg);
  }
  .pouch-front {
    position: absolute;
    left: 190px;
    top: 205px;
    width: 580px;
    height: 800px;
    background: linear-gradient(35deg, var(--butter) 0%, var(--cream) 30%, var(--pouch-white) 62%);
    border-radius: 6px;
    overflow: hidden;
    box-shadow: 0 0 0 1px #eeeae0;
  }
  .swoosh {
    position: absolute;
    inset: 0;
    width: 580px;
    height: 800px;
  }
  .brand-name {
    position: absolute;
    left: 0;
    width: 580px;
    top: 172px;
    text-align: center;
    font-family: "Quicksand", sans-serif;
    font-weight: 600;
    font-size: 52px;
    letter-spacing: -1px;
    color: var(--brand-blue);
    z-index: 2;
  }
  .product-title {
    position: absolute;
    font-family: "Damion", cursive;
    line-height: 1;
    white-space: nowrap;
    z-index: 2;
  }
  .product-title--ginger {
    left: 98px;
    top: 245px;
    font-size: 156px;
    color: var(--ginger-orange);
  }
  .product-title--candy {
    left: 215px;
    top: 362px;
    font-size: 108px;
    color: var(--candy-yellow);
  }
  .tagline {
    position: absolute;
    left: 303px;
    top: 492px;
    width: 270px;
    font-family: "Quicksand", sans-serif;
    font-weight: 600;
    font-size: 20px;
    line-height: 1.7;
    color: var(--leaf-green);
    z-index: 3;
  }
  .tagline span { display: block; white-space: nowrap; }
  .tagline span + span { padding-left: 6px; }
  .net-weight {
    position: absolute;
    left: 414px;
    top: 657px;
    font-family: "Quicksand", sans-serif;
    font-weight: 500;
    font-size: 30px;
    color: var(--brand-blue);
    z-index: 2;
  }
  .ginger-art {
    position: absolute;
    left: 95px;
    top: 480px;
    width: 295px;
    height: 300px;
    border-radius: 45% 20% 50% 50%;
    background: radial-gradient(ellipse at 45% 60%, var(--slice-yellow) 0%, var(--root-tan) 50%, rgba(226,185,143,0) 75%);
    z-index: 1;
  }
</style>
</head>
<body>
<main class="canvas">
  <section class="pouch-front">
    <svg class="swoosh" viewBox="0 0 580 800" aria-hidden="true">
      <path d="M580 10 C 520 120, 330 110, 220 210 C 120 300, 150 420, 80 520 C 40 580, 10 640, 0 690 L 0 800 L 0 480 C 30 380, 40 300, 140 220 C 260 120, 470 140, 580 60 Z" fill="#fff3d1" opacity="0.9"/>
    </svg>
    <div class="brand-name">Tolvo</div>
    <div class="product-title product-title--ginger">Ginger</div>
    <div class="product-title product-title--candy">Candy</div>
    <div class="ginger-art" role="img" aria-label="Illustration of a fresh ginger root with two green leaves and sliced ginger pieces"></div>
    <p class="tagline"><span>a good relief for sore</span><span>throat and nausea.</span></p>
    <div class="net-weight">4oz</div>
  </section>
</main>
</body>
</html>
```